Website design for Keystone Stewardship Australia, a new boutique specialist consultancy company

We need a web design for a new company based in Australia called Keystone Stewardship Australia (this is abbreviated in our logo to KSA).

KSA is a boutique specialist advisory firm that provides Interim Management and Executive Transition Services. Through a suite of best practice methodologies coupled with advisory and consulting services, KSA supports businesses and executives during times of leadership hiatus and transition which not only mitigates risk of transition failure, but more importantly accelerates transition success.

Delphine at PixelHarbor has designed our logo (see attached file) and the logo and its colours will guide the website design. The primary colour scheme will be in the turquoise/aqua range and may include accent colours - designer's creative choice and guidance is welcome here.

The website should convey an image of crisp, modern professionalism. It's purpose will be to provide information about the company, our products and services and provide contact details. There is no online ordering or payment functionality required. Pages will include a home page with general information about the company, a number of content pages outlining information about each aspect of the services offered, an "about us" page and a "contact us" page.

Target Market(s)

This is a Busines-to-Business company and our target market is primarily large and medium sized companies. The specific individuals targeted at these companies will include:

Human Resources Directors
Talent and Recruitment Heads
Boards and Senior Executive teams of companies
Hiring managers responsible for recruiting and managing senior leaders and executives

Industry/Entity Type

Boutique

Requirements
Should not have
• Online ordering / payment page

```html
<!DOCTYPE html>
<html lang="en">
<head>
<meta charset="utf-8">
<title>Keystone Stewardship Australia</title>
<link href="https://fonts.googleapis.com/css2?family=Oxygen:wght@400;700&family=Lora:ital,wght@1,400&family=Cinzel:wght@500&display=swap" rel="stylesheet">
<style>
:root{
  --teal:#72bcc6;
  --teal-dark:#2f7f88;
  --teal-text:#3a8c95;
  --orange:#e65a1f;
  --ink:#333;
  --band:#f4f4f4;
  --white:#fff;
  --navy:#2a4f8f;
}
*{box-sizing:border-box;margin:0;padding:0}
html,body{width:911px;height:1200px;overflow:hidden}
body{position:relative;background:var(--white);font-family:'Oxygen',Arial,sans-serif;color:var(--ink)}
.abs{position:absolute}

/* header */
.site-header{position:absolute;left:0;top:0;width:911px;height:128px;background:linear-gradient(#fff,#f7f8f8)}
.brand{left:101px;top:12px;display:flex;align-items:center;height:56px}
.brand-name{font-size:40px;font-weight:700;color:var(--teal);line-height:56px;letter-spacing:1px}
.brand-divider{width:1px;height:50px;background:var(--teal-dark);margin:0 9px 0 14px}
.brand-full{font-size:14px;line-height:15.5px;color:var(--teal-dark)}
.phone{left:689px;top:10px;display:flex;align-items:center;font-size:14px;color:var(--ink)}
.phone-icon{width:22px;height:22px;border-radius:50%;background:var(--orange);margin-right:5px;display:flex;align-items:center;justify-content:center}
.search{left:657px;top:45px;width:153px;height:22px;border:1px solid #cfcfcf;border-radius:3px;background:#f3f3f3;font-size:10px;color:#777;padding:4px 8px;letter-spacing:.5px}
.search-btn{position:absolute;right:0;top:0;width:26px;height:20px;border-left:1px solid #cfcfcf;display:flex;align-items:center;justify-content:center}

.main-nav{left:100px;top:84px;width:711px;height:32px;background:var(--teal);display:flex}
.main-nav a{display:flex;align-items:center;justify-content:center;color:var(--white);font-size:11px;font-weight:700;text-decoration:none;letter-spacing:.3px;border-left:1px solid rgba(255,255,255,.35)}
.main-nav a.active{background:var(--orange);border-left:none}

/* hero */
.hero{left:100px;top:128px;width:711px;height:277px;background:linear-gradient(115deg,#dcdcda 0%,#bdbdba 55%,#8b8b88 100%)}
.hero-caption{right:9px;top:185px;width:292px;height:54px;background:rgba(114,188,198,.9);color:var(--white);font-family:'Lora',Georgia,serif;font-style:italic;font-size:18.5px;line-height:22px;text-align:right;padding:5px 8px 0 0;white-space:nowrap}
.dots{display:flex;gap:4px}
.dot{width:10px;height:10px;border-radius:50%;border:1px solid #bbb;background:var(--white)}
.dot.on{background:var(--orange);border-color:var(--orange)}

/* service cards */
.card{top:430px;width:221px;height:149px;border:1px solid #c9c9c9;border-radius:4px;background:linear-gradient(#fff,#eef5f6);box-shadow:0 5px 6px -3px rgba(0,0,0,.25)}
.card-img{position:absolute;left:6px;top:6px;width:207px;height:98px;border-radius:4px}
.card-title{position:absolute;left:0;top:110px;width:100%;text-align:center;font-size:14px;line-height:16px;letter-spacing:.8px;color:var(--teal-text)}
.card-title span{display:block;color:var(--orange)}

/* welcome */
.welcome{left:101px;top:612px;width:475px}
.welcome h1{font-size:19px;font-weight:400;color:var(--teal-dark);height:38px;display:flex;align-items:flex-end;padding-bottom:4px;border-bottom:1px solid #bbb}
.welcome h1 b{color:var(--teal);font-size:24px;margin-left:6px;line-height:26px}
.welcome-text{margin-top:7px;font-size:11px;line-height:17.2px;color:#2c2c2c}
.welcome-text span{display:block;white-space:nowrap;text-align:justify;text-align-last:justify}
.welcome-text span.last{text-align-last:left}
.read-more{display:block;margin-top:12px;font-size:11px;font-weight:700;color:var(--orange);text-decoration:none}
.col-rule{left:594px;top:612px;width:1px;height:180px;background:linear-gradient(#fff,#ddd,#fff)}

/* opinions */
.opinions{left:612px;top:607px;width:199px}
.opinions h2{font-size:19px;font-weight:400;color:var(--teal-dark);height:30px;display:flex;align-items:center;border-bottom:1px solid #bbb}
.avatar{left:614px;top:642px;width:66px;height:66px;border-radius:50%;border:3px solid var(--teal);background:radial-gradient(#d9b79d,#8a6a57)}
.person{left:691px;top:661px;font-size:11px;line-height:16px}
.person b{color:var(--teal-text)}
.quote-box{left:612px;top:718px;width:199px;height:83px;border:1px solid #e2e2e2;padding:11px 0 0 25px;font-style:italic;font-size:9.2px;line-height:15px;color:#444;white-space:nowrap}
.qmark{font-family:Georgia,serif;font-size:26px;color:#bbb;font-style:normal;line-height:1}

/* additional services */
.extras{left:0;top:817px;width:911px;height:152px;background:var(--band);border-top:1px solid #e4e4e4;border-bottom:2px solid var(--orange)}
.extras-title{left:320px;top:-1px;width:270px;height:26px}
.extras-title span{position:absolute;left:0;top:2px;width:100%;text-align:center;font-family:'Cinzel',Georgia,serif;font-size:17px;letter-spacing:1px;color:var(--white)}
.extra{top:50px;display:flex;align-items:center}
.extra-icon{width:66px;height:66px;border-radius:50%;background:radial-gradient(#fff 55%,#e8e8e8);border:1px solid #ddd;box-shadow:0 6px 5px -4px rgba(0,0,0,.2);display:flex;align-items:center;justify-content:center;margin-right:10px}
.extra-name{font-size:14.5px;line-height:16px;color:var(--teal-text);text-align:center}
.extra-name span{display:block;color:var(--orange)}

/* footer */
.site-footer{left:0;top:969px;width:911px;height:231px;background:var(--teal);color:var(--white)}
.site-footer h3{position:absolute;top:14px;font-size:13px;font-weight:400}
.dash{left:0;top:39px;width:911px;border-top:1px dashed rgba(255,255,255,.45)}
.vrule{top:50px;width:1px;height:130px;background:rgba(0,0,0,.1)}
.quick-links{left:101px;top:43px;list-style:none;width:80px}
.quick-links li{height:25px;line-height:24px;font-size:10px;border-bottom:1px solid rgba(255,255,255,.3)}
.quick-links li:last-child{border-bottom:none}
.quick-links li::before{content:"›";margin-right:7px}
.contact{left:343px;top:48px;font-size:10px;line-height:15px;font-style:normal}
.contact-row{display:flex;align-items:center;gap:6px;margin-top:12px}
.field{left:644px;width:167px;height:22px;background:var(--white);border:1px solid #9cc;font-size:10px;font-style:italic;color:#888;padding:4px 7px}
.submit{left:644px;top:163px;width:62px;height:21px;background:var(--orange);color:var(--white);font-size:11px;font-weight:700;display:flex;align-items:center;justify-content:center}
.copyright{left:100px;top:205px;font-size:10px}
.follow{left:645px;top:199px;display:flex;align-items:center;gap:6px;font-size:10px;font-style:italic}
.social{width:23px;height:23px;border-radius:3px;background:var(--navy);border:1px solid rgba(255,255,255,.5)}
</style>
</head>
<body>

<header class="site-header">
  <div class="abs brand">
    <span class="brand-name">KSA</span>
    <span class="brand-divider"></span>
    <span class="brand-full">Keystone<br>Stewardship<br>Australia Pty Ltd</span>
  </div>
  <div class="abs phone">
    <span class="phone-icon"><svg width="12" height="12" viewBox="0 0 24 24"><path fill="#fff" d="M6.6 10.8c1.4 2.8 3.8 5.1 6.6 6.6l2.2-2.2c.3-.3.7-.4 1-.2 1.1.4 2.3.6 3.6.6.6 0 1 .4 1 1V20c0 .6-.4 1-1 1C10.6 21 3 13.4 3 4c0-.6.4-1 1-1h3.5c.6 0 1 .4 1 1 0 1.3.2 2.5.6 3.6.1.3 0 .7-.2 1z"/></svg></span>
    +61 2 5550 1842
  </div>
  <div class="abs search">Search..
    <span class="search-btn"><svg width="12" height="12" viewBox="0 0 12 12"><circle cx="5" cy="5" r="3.8" fill="none" stroke="#444" stroke-width="1.4"/><line x1="7.8" y1="7.8" x2="11" y2="11" stroke="#444" stroke-width="1.6"/></svg></span>
  </div>
  <nav class="abs main-nav">
    <a class="active" style="width:93px">HOME</a>
    <a style="width:118px">ABOUT US</a>
    <a style="width:114px">SERVICES</a>
    <a style="width:114px">SUPPORT</a>
    <a style="width:126px">PARTNERS</a>
    <a style="width:146px">CONTACT US</a>
  </nav>
</header>

<section class="abs hero" role="img" aria-label="Businessman in a suit standing on a staircase climbing a grey wall, the steps ahead crumbling away">
  <div class="abs hero-caption">Lorem ipsum dolor sit amet<br>consect adipiscing elit sed diam</div>
  <div class="abs dots" style="left:329px;top:251px"><span class="dot on"></span><span class="dot"></span><span class="dot"></span><span class="dot"></span></div>
</section>

<article class="abs card" style="left:100px">
  <div class="card-img" role="img" aria-label="Open hand bridging a gap between two stone pillars against a city skyline" style="background:linear-gradient(#7c9bbb,#c7d3dc 70%,#a49c8c)"></div>
  <div class="card-title">Interim Management<span>Services</span></div>
</article>
<article class="abs card" style="left:346px">
  <div class="card-img" role="img" aria-label="Magnifying glass over a printed bar chart report" style="background:linear-gradient(120deg,#1e2630,#556170 55%,#202830)"></div>
  <div class="card-title">Transition<span>Review</span></div>
</article>
<article class="abs card" style="left:591px">
  <div class="card-img" role="img" aria-label="Businessman stepping onto a sketched bridge against a cloudy sky" style="background:linear-gradient(#4f86b8,#b9cfe0 65%,#8d949a)"></div>
  <div class="card-title">Transition<span>Support</span></div>
</article>

<section class="abs welcome">
  <h1>Welcome to <b>KSA</b></h1>
  <p class="welcome-text">
    <span>Lorem ipsum dolor sit amet, consectetuer adipiscing elit, sed diam nonummy nibh euismod</span>
    <span>tinciduntm ut laoreet dolore magna aliquam erat volutpat. Ut wisi enim ad minim veniam, quis</span>
    <span>nostrud exerciosgi tation ullamcorper suscipit lobortis nisl ut aliquip ex ea commodo consequat.</span>
    <span>Duis autem vel eumsodn iriure dolor in hendrerit in vulputate velit esse molestie consequat, vel</span>
    <span>illum dolore eu feugiat nullamo facilisis at vero eros et accumsan et iusto odio dignissim qui</span>
    <span>Lorem ipsum dolor sit amet, consectetuer adipiscing elit, sed diam nonummy nibh euismod</span>
    <span class="last">tinciduntm ut laoreet dolore magna aliquam erat volutpat.</span>
  </p>
  <a class="read-more">Read More »</a>
</section>
<div class="abs col-rule"></div>

<section class="abs opinions">
  <h2><svg width="24" height="22" viewBox="0 0 24 22" style="margin-right:6px"><rect x="0" y="0" width="16" height="12" rx="2" fill="var(--orange)"/><path d="M3 12 L3 17 L8 12Z" fill="var(--orange)"/><rect x="8" y="7" width="15" height="10" rx="2" fill="#f28a5c"/><path d="M19 17 L20 21 L15 17Z" fill="#f28a5c"/></svg>Opinions</h2>
</section>
<div class="abs avatar" role="img" aria-label="Portrait photo of the client giving the testimonial"></div>
<div class="abs person"><b>Marcus Teller</b><br>Bussiness Man</div>
<blockquote class="abs quote-box">
  <span class="qmark abs" style="left:8px;top:8px">“</span>
  Ut wisi enim ad minim veniam, quism<br>nostrli erci tation ullamcorper suscipitop<br>lobortis commodo consequat.
  <span class="qmark abs" style="left:146px;top:42px">”</span>
  <div class="abs dots" style="left:154px;top:67px;gap:3px"><span class="dot" style="width:6px;height:6px;background:#ccc;border:none"></span><span class="dot on" style="width:6px;height:6px;border:none"></span><span class="dot" style="width:6px;height:6px;background:#ccc;border:none"></span><span class="dot" style="width:6px;height:6px;background:#ccc;border:none"></span></div>
</blockquote>
<svg class="abs" style="left:660px;top:710px" width="22" height="10" viewBox="0 0 22 10"><path d="M0 9 L11 0 L22 9" fill="#fff" stroke="#e2e2e2"/><rect x="0" y="9" width="22" height="2" fill="#fff"/></svg>

<section class="abs extras">
  <div class="abs extras-title">
    <svg width="270" height="26" viewBox="0 0 270 26"><path d="M0 0 H270 L258 13 L246 26 H24 L12 13Z" fill="var(--teal)"/></svg>
    <span>Additional Services</span>
  </div>
  <div class="abs extra" style="left:108px">
    <div class="extra-icon"><svg width="34" height="40" viewBox="0 0 34 40"><circle cx="17" cy="9" r="7" fill="#f07a52"/><path d="M2 38 V26 Q2 19 10 19 H24 Q32 19 32 26 V38Z" fill="var(--teal)"/><path d="M15 19 L17 32 L19 19Z" fill="#f07a52"/></svg></div>
    <div class="extra-name">Executive<span>Search</span></div>
  </div>
  <div class="abs extra" style="left:296px">
    <div class="extra-icon"><svg width="42" height="40" viewBox="0 0 42 40"><rect x="13" y="0" width="16" height="10" rx="4" fill="#f07a52"/><circle cx="11" cy="18" r="5" fill="var(--teal)"/><circle cx="31" cy="18" r="5" fill="var(--teal)"/><rect x="3" y="25" width="16" height="14" rx="4" fill="var(--teal)"/><rect x="23" y="25" width="16" height="14" rx="4" fill="var(--teal)"/></svg></div>
    <div class="extra-name">Advisory &amp; Consulting<span>Services</span></div>
  </div>
  <div class="abs extra" style="left:566px">
    <div class="extra-icon"><svg width="42" height="40" viewBox="0 0 42 40"><rect x="20" y="2" width="20" height="15" rx="1" fill="var(--teal)"/><circle cx="10" cy="10" r="4" fill="#f07a52"/><path d="M4 24 Q4 16 10 16 Q14 16 20 12 L21 14 Q16 19 15 24Z" fill="#f07a52"/><circle cx="14" cy="28" r="3.5" fill="#f07a52"/><circle cx="28" cy="28" r="3.5" fill="#f07a52"/><rect x="8" y="32" width="12" height="7" rx="3" fill="#f07a52"/><rect x="22" y="32" width="12" height="7" rx="3" fill="#f07a52"/></svg></div>
    <div class="extra-name">Training &amp; Development<span>Services</span></div>
  </div>
</section>

<footer class="abs site-footer">
  <h3 style="left:101px">Quick Links</h3>
  <h3 style="left:343px">Contact Details</h3>
  <h3 style="left:645px">Quick Contact</h3>
  <div class="abs dash"></div>
  <div class="abs vrule" style="left:257px"></div>
  <div class="abs vrule" style="left:558px"></div>
  <ul class="abs quick-links">
    <li>Home</li><li>About Us</li><li>Services</li><li>Support</li><li>Partners</li><li>Contact Us</li>
  </ul>
  <address class="abs contact">
    <b>Keystone Stewardship<br>Australia Pty Ltd</b><br>
    16 Harbour Lane, Suite 4<br>Parramatta, NSW 2150
    <div class="contact-row" style="margin-top:12px"><svg width="10" height="10" viewBox="0 0 24 24"><path fill="#2f6a72" d="M6.6 10.8c1.4 2.8 3.8 5.1 6.6 6.6l2.2-2.2c.3-.3.7-.4 1-.2 1.1.4 2.3.6 3.6.6.6 0 1 .4 1 1V20c0 .6-.4 1-1 1C10.6 21 3 13.4 3 4c0-.6.4-1 1-1h3.5c.6 0 1 .4 1 1 0 1.3.2 2.5.6 3.6.1.3 0 .7-.2 1z"/></svg>555-210-4417</div>
    <div class="contact-row"><svg width="11" height="10" viewBox="0 0 11 10"><rect x="3" y="0" width="5" height="3" fill="#2f6a72"/><rect x="0" y="3" width="11" height="5" rx="1" fill="#2f6a72"/><rect x="3" y="6" width="5" height="4" fill="#cfe"/></svg>555-210-4418</div>
    <div class="contact-row"><svg width="11" height="8" viewBox="0 0 11 8"><rect width="11" height="8" fill="#2f6a72"/><path d="M0 0 L5.5 4.5 L11 0" fill="none" stroke="#cfe"/></svg>hello@ksa.au</div>
  </address>
  <div class="abs field" style="top:52px">Name</div>
  <div class="abs field" style="top:81px">Email</div>
  <div class="abs field" style="top:109px;height:47px">Message</div>
  <div class="abs submit">SUBMIT</div>
  <div class="abs copyright">© 2014 Keystone Stewardship Australia Pty Ltd. All Rights Reserved.</div>
  <div class="abs follow">Follow Us: <span class="social" style="margin-left:4px" aria-label="Social profile"></span><span class="social" aria-label="Professional network profile"></span></div>
</footer>

</body>
</html>
```